Book cover needed for Christian Non-Fiction Book

I need book cover design (eBook , Paperback, and possibly case laminate Hardcover) for use on Folvane Press and Corvel Print.
Title: Bound for Shore
Sub-Title: Leaving Harbors and Walking in Quiet Trust
Author: Neil Varden
Also on front cover "Forward by R. Leona Pask"

I like clean/simple designs. Below are links to examples of covers I like...
https://www.shelvora.example/dp/Q4821MZT0X?tag=kelvpage-20&linkCode=ogi&th=1&psc=1
https://www.shelvora.example/dp/Q48HTRNWAC?tag=kelvpage-20&linkCode=ogi&th=1&psc=1
https://www.shelvora.example/dp/Q22FKD93XJ?tag=kelvpage-20&linkCode=ogi&th=1&psc=1
https://www.shelvora.example/dp/Q48W3PLMHD?tag=kelvpage-20&linkCode=ogi&th=1&psc=1
https://www.shelvora.example/dp/Q48R5ZZCQN?tag=kelvpage-20&linkCode=ogi&th=1&psc=1
https://www.shelvora.example/dp/Q22H0KKPU7?tag=kelvpage-20&linkCode=ogi&th=1&psc=1

The main idea for Bound for Shore is that God is a sending God and being "on the move" or journeying is central to God's character, and therefore God's people. I write about our hesitancy to "go," and how the Bible is full of stories about people "going" from Abraham to Jesus, to the disciples of Jesus.

The core biblical text is the Great Commission in Matthew 28:16-20, where Jesus sends out his followers, though some of them doubt.

This paragraph from the forward by R. Leona Pask captures the tone of the book well:
This book is a call amid the turmoil. Sacred scripture contains no shortage of narratives in which humans are pulled from their ordinary lives with an inciting incident whose stakes are high. These Biblical figures are lulled from complacency and comfort zones—and yet they are reluctant to serve because they question their ability and influence. Their lessons are relevant for us today: They, and we, are always called and sent with authority. The power of the Holy Spirit equips their “going”—and ours. It’s a sending out that looks less like mastery and more humility. It’s a sending out that is unequivocal service to others modelled in a rabbi-reformer who washed feet and touched the unclean.

I have previously published two shorter books and would be very interested in getting new covers for the old books these so that the three have a similar feel. Whichever designer I go with for "Bound for Shore" I would also want to work with on creating a "branded look" for the other two books.

Target Market(s)

Christian, Religion, Spirituality Readers

Requirements
Must have
• The front cover must have this copy...
Bound for Shore
Leaving Harbors and Walking in Quiet Trust
Neil Varden
Forward by R. Leona Pask

Must be willing to do the full paperback and/or hardcover, but start with thefront cover please
Nice to have
• See attached files for some book covers I like

```html
<!DOCTYPE html>
<html lang="en">
<head>
<meta charset="utf-8">
<title>Bound for Shore — Full Cover</title>
<link rel="stylesheet" href="https://fonts.googleapis.com/css2?family=Parisienne&family=IM+Fell+English+SC&family=Alegreya+Sans:wght@400;500&family=Raleway:wght@400;500&display=swap">
<style>
  :root {
    --page-bg: #000000;
    --cover-cream: #f1f1df;
    --cover-edge: #8fa3ad;
    --title-rust: #c0501a;
    --title-white: #ffffff;
    --subtitle-red: #8c1236;
    --author-red: #9b1020;
    --body-ink: #1e1e1e;
    --credit-ink: #2f2f2f;
    --spine-ink: #151515;
    --beam-cyan: #8fe0f0;
    --beam-yellow: #fbe86a;
    --beam-pink: #f5b6c6;
  }
  * { margin: 0; padding: 0; box-sizing: border-box; }
  html, body { width: 1200px; height: 751px; overflow: hidden; background: var(--page-bg); }
  .canvas { position: relative; width: 1200px; height: 751px; background: var(--page-bg); }

  .cover {
    position: absolute; left: 90px; top: 11px; width: 1020px; height: 729px; overflow: hidden;
    background:
      radial-gradient(ellipse 70% 72% at 50% 50%, var(--cover-cream) 45%, #e6e9d8 68%, var(--cover-edge) 100%);
  }
  .light-beams {
    position: absolute; left: 480px; top: -120px; width: 700px; height: 1000px;
    background: linear-gradient(120deg,
      transparent 22%, rgba(143,224,240,.75) 32%, rgba(251,232,106,.85) 46%,
      rgba(251,222,110,.7) 54%, rgba(245,182,198,.6) 64%, transparent 74%);
    filter: blur(18px); opacity: .85;
  }

  .title { position: absolute; text-align: center; }
  .title-script { display: block; font-family: "Parisienne", cursive; line-height: 1; }
  .title-caps { display: block; font-family: "IM Fell English SC", serif; line-height: 1; }

  .back-title { left: 155px; top: 98px; width: 360px; color: var(--title-rust); }
  .back-title .title-script { font-size: 52px; }
  .back-title .title-caps { font-size: 50px; margin-top: -4px; }

  .back-blurb {
    position: absolute; left: 101px; top: 261px; width: 280px;
    font-family: "Alegreya Sans", sans-serif; font-size: 11px; line-height: 16.3px; color: var(--body-ink);
  }

  .spine-text {
    position: absolute; left: 498px; width: 24px;
    writing-mode: vertical-rl; font-family: "Raleway", sans-serif; font-weight: 500;
    font-size: 19px; letter-spacing: 1px; color: var(--spine-ink); line-height: 24px;
  }
  .spine-title { top: 66px; }
  .spine-author { top: 505px; }

  .front-title { left: 580px; top: 82px; width: 400px; color: var(--title-white); text-shadow: 2px 3px 6px rgba(0,0,0,.45); }
  .front-title .title-script { font-size: 62px; }
  .front-title .title-caps { font-size: 60px; margin-top: -2px; }

  .front-subtitle {
    position: absolute; left: 560px; top: 245px; width: 440px; text-align: center;
    font-family: "Alegreya Sans", sans-serif; font-weight: 500; font-size: 16.5px; color: var(--subtitle-red);
  }

  .communion-art {
    position: absolute; left: 666px; top: 293px; width: 200px; height: 230px;
    border-radius: 40% 40% 30% 30%;
    background: radial-gradient(ellipse at 45% 60%, rgba(160,110,60,.55) 0%, rgba(200,195,185,.45) 45%, rgba(255,255,255,0) 72%);
  }

  .foreword-credit {
    position: absolute; left: 580px; top: 615px; width: 400px; text-align: center;
    font-family: "Raleway", sans-serif; font-size: 22px; color: var(--credit-ink);
  }
  .author-name {
    position: absolute; left: 580px; top: 653px; width: 400px; text-align: center;
    font-family: "Raleway", sans-serif; font-weight: 500; font-size: 29px; color: var(--author-red); letter-spacing: .5px;
  }
</style>
</head>
<body>
<div class="canvas">
  <section class="cover">
    <div class="light-beams" aria-hidden="true"></div>

    <div class="back-cover">
      <h2 class="title back-title"><span class="title-script">Bound for</span><span class="title-caps">Shore</span></h2>
      <p class="back-blurb">This book is a call amid the turmoil. Sacred scripture contains no shortage of narratives in which humans are pulled from their ordinary lives with an inciting incident whose stakes are high. These Biblical figures are lulled from complacency and comfort zones—and yet they are reluctant to serve because they question their ability and influence. Their lessons are relevant for us today: They, and we, are always called and sent with authority. The power of the Holy Spirit equips their “going”—and ours. It’s a sending out that looks less like mastery and more humility. It’s a sending out that is unequivocal service to others modelled in a rabbi-reformer who washed feet and touched the unclean.</p>
    </div>

    <div class="spine">
      <span class="spine-text spine-title">BOUND FOR SHORE</span>
      <span class="spine-text spine-author">NEIL VARDEN</span>
    </div>

    <div class="front-cover">
      <h1 class="title front-title"><span class="title-script">Bound for</span><span class="title-caps">Shore</span></h1>
      <p class="front-subtitle">Leaving Harbors and Walking in Quiet Trust</p>
      <div class="communion-art" role="img" aria-label="Photograph of a loaf of bread and a silver chalice"></div>
      <p class="foreword-credit">Forward by R. Leona Pask</p>
      <p class="author-name">NEIL VARDEN</p>
    </div>
  </section>
</div>
</body>
</html>
```